Premium modern eliquids labels 84.5 x 80 mm

I am looking for modern graphics for the labels of a new eliquid line that will have 4 different types of eliquids. It will have a tobacco one (brown colours maybe), a fruity one (bright colours maybe), a minty one (green colours maybe) and a creamy one (beige colours maybe).
I will need one of them to see how the design is, that design will have to be adapted to the other 3 colours of the label.
The brand logo is attached. I also attached a sample of what is mandatory to write on the label, you can change size, place and font of what is written, the only thing that cannot be reduced is the yellow parts. I attach the bottle that we will use.The size of the label is 84.5 x 80 mm (base x height).

Target Market(s)

vapers

Requirements
Must have
• My project must have one of the labels.

```html
<!DOCTYPE html>
<html lang="it">
<head>
<meta charset="utf-8">
<title>Verdant Drop – Kiwi Flavour label</title>
<link href="https://fonts.googleapis.com/css2?family=Montserrat:wght@500;700;800&display=swap" rel="stylesheet">
<style>
  :root {
    --bg: #5a6e45;
    --green-light: #8fd14a;
    --green-dark: #2db54c;
    --green-pill: #3dba4e;
    --white: #ffffff;
    --brand-blue: #3d9fd9;
    --ink: #2b2b2b;
    --warn-yellow: #f7c21a;
    --kiwi-flesh: #9cc33a;
    --kiwi-skin: #8a6a3a;
  }
  * { box-sizing: border-box; margin: 0; padding: 0; }
  html, body { width: 1200px; height: 874px; overflow: hidden; }
  body {
    background: var(--bg);
    font-family: "Montserrat", sans-serif;
    position: relative;
  }
  .label {
    position: absolute;
    left: 220px; top: 77px;
    width: 760px; height: 720px;
    background: linear-gradient(180deg, var(--green-light) 0%, var(--green-dark) 100%);
    overflow: hidden;
  }
  /* left info strip */
  .info-left {
    position: absolute; left: 30px; top: 60px;
    width: 130px; height: 600px;
  }
  .info-left .vertical {
    position: absolute;
    writing-mode: vertical-rl;
    transform: rotate(180deg);
    color: var(--ink);
    font-size: 13px; font-weight: 500; line-height: 1.4;
  }
  .ingredients { left: 8px; top: 120px; height: 380px; }
  .lot-box {
    left: 64px; top: 60px; height: 440px;
    border: 1.5px solid var(--ink); padding: 10px 6px;
    font-size: 12px;
  }
  .bin-icon { position: absolute; left: 20px; bottom: 10px; }
  /* central oval */
  .front {
    position: absolute; left: 190px; top: 40px;
    width: 380px; height: 640px;
    background: var(--white);
    border-radius: 50%;
  }
  .brand {
    position: absolute; top: 150px; left: 0; width: 100%;
    text-align: center;
    font-size: 34px; font-weight: 800; letter-spacing: 1px;
    color: var(--brand-blue);
  }
  .brand-dot {
    display: inline-block; width: 14px; height: 14px;
    background: var(--brand-blue); border-radius: 50%;
    margin-left: 6px; vertical-align: middle;
  }
  .fruit-photo {
    position: absolute; left: 95px; top: 235px;
    width: 190px; height: 180px; border-radius: 50%;
    background: radial-gradient(circle at 50% 45%, var(--kiwi-flesh) 0%, #6f9a2c 55%, var(--kiwi-skin) 100%);
  }
  .flavour-pill {
    position: absolute; left: 55px; top: 440px;
    width: 270px; height: 52px; border-radius: 12px;
    background: var(--green-pill); color: var(--white);
    font-size: 26px; font-weight: 700;
    display: flex; align-items: center; justify-content: center;
  }
  .volume { position: absolute; left: 150px; top: 512px; }
  /* right info strip */
  .info-right {
    position: absolute; left: 600px; top: 60px;
    width: 140px; height: 600px;
  }
  .warn {
    background: var(--warn-yellow); color: var(--ink);
    font-size: 13px; font-weight: 800; line-height: 1.25;
    padding: 10px 8px; margin-bottom: 14px;
  }
  .producer {
    color: var(--ink); font-size: 12px; font-weight: 500; line-height: 1.45;
    margin-top: 10px;
  }
  .age {
    margin-top: 24px;
    width: 64px; height: 64px; border-radius: 50%;
    background: var(--white); border: 3px solid var(--ink);
    color: var(--ink); font-weight: 800; font-size: 22px;
    display: flex; align-items: center; justify-content: center;
  }
</style>
</head>
<body>
  <main class="label">
    <section class="info-left">
      <p class="vertical ingredients">INGREDIENTI: GLICOLE PROPILENICO, SOSTANZE AROMATIZZANTI</p>
      <p class="vertical lot-box">L 5H00 / 001 &nbsp; PROD 22-04-2022 &nbsp; DC 21-04-2024</p>
      <svg class="bin-icon" width="28" height="40" viewBox="0 0 28 40" aria-label="Recycle bin">
        <circle cx="14" cy="5" r="4" fill="var(--ink)"/>
        <path d="M4 12 H24 L21 38 H7 Z" fill="none" stroke="var(--ink)" stroke-width="2.5"/>
      </svg>
    </section>

    <section class="front">
      <div class="brand">VERDANT DROP<span class="brand-dot"></span></div>
      <div class="fruit-photo" role="img" aria-label="Photo of sliced kiwi fruit halves with a leaf"></div>
      <div class="flavour-pill">KIWI FLAVOUR</div>
      <svg class="volume" width="80" height="110" viewBox="0 0 80 110" aria-label="20 ml net">
        <path d="M40 2 C50 25 76 48 76 72 A36 36 0 0 1 4 72 C4 48 30 25 40 2 Z" fill="var(--green-pill)"/>
        <text x="40" y="70" text-anchor="middle" fill="#fff" font-family="Montserrat, sans-serif" font-weight="700" font-size="16">20ML</text>
        <text x="40" y="90" text-anchor="middle" fill="#fff" font-family="Montserrat, sans-serif" font-weight="700" font-size="16">NET</text>
      </svg>
    </section>

    <section class="info-right">
      <p class="warn">ATTENZIONE: CONTIENE SOSTANZE NOCIVE SE INGERITE.</p>
      <p class="warn">TENERE FUORI DALLA PORTATA DEI BAMBINI</p>
      <p class="producer">Prodotto da Nordvale Srl<br>Via dei Tigli 14, 20100 Milano<br>info@nordvale.it</p>
      <div class="age">18+</div>
    </section>
  </main>
</body>
</html>
```